Letterhead Design Project

Attached is our new Logo and a copy of our old letter head
Looking to rebrand with our new logo

Reason: I want to show a business card design

Industry/Entity Type

Film Production

Colors

Designer to choose colors to be used in the design.

Requirements
Must have
• The information on the old letterhead

```html
<!DOCTYPE html>
<html lang="en">
<head>
<meta charset="utf-8">
<title>Korro International – Letterhead</title>
<link href="https://fonts.googleapis.com/css2?family=Montserrat:wght@400;600;700&display=swap" rel="stylesheet">
<style>
  :root {
    --navy: #0f4a6e;
    --blue: #1a86b8;
    --sky: #2aaee0;
    --orange: #e8692a;
    --divider: #5fb6e0;
    --faint: #eef4f8;
    --paper: #ffffff;
  }
  * { margin: 0; padding: 0; box-sizing: border-box; }
  html, body { width: 848px; height: 1200px; overflow: hidden; background: var(--paper); }
  body { font-family: "Montserrat", Arial, sans-serif; }
  .letterhead { position: relative; width: 848px; height: 1200px; background: var(--paper); }

  .brand-name {
    position: absolute; left: 55px; top: 62px; width: 160px;
    color: var(--navy); font-weight: 700; font-size: 30px; line-height: 1.05;
    letter-spacing: 1px;
  }
  .brand-name span { display: block; font-size: 14.5px; letter-spacing: 2.2px; margin-top: 8px; }

  .header-divider {
    position: absolute; left: 245px; top: 37px; width: 2px; height: 94px; background: var(--divider);
  }
  .header-info { position: absolute; left: 285px; top: 53px; color: var(--navy); }
  .header-tagline { color: var(--orange); font-weight: 700; font-size: 18.5px; margin-bottom: 5px; }
  .header-address { font-size: 16px; margin-bottom: 6px; }
  .header-contact { font-size: 14.5px; }
  .header-contact b { font-weight: 700; }
  .header-contact .gap { display: inline-block; width: 12px; }

  .watermark {
    position: absolute; left: 0; top: 590px; width: 848px; text-align: center;
    color: var(--faint); font-weight: 700; line-height: 1;
  }
  .watermark-name { font-size: 120px; letter-spacing: 4px; }
  .watermark-sub { font-size: 40px; letter-spacing: 12px; margin-top: 18px; }

  .footer-wave { position: absolute; left: 0; top: 1040px; width: 848px; height: 160px; }
  .footer-text { position: absolute; left: 78px; top: 1114px; color: #fff; font-size: 12.5px; line-height: 17px; }
  .footer-text .divisions { font-weight: 700; font-size: 13px; }
  .footer-text .owner { font-size: 11.5px; }
  .footer-text .owner b { color: #f7941d; font-weight: 700; font-size: 13px; margin-left: 3px; }
  .footer-text .registration { font-size: 11.5px; }
</style>
</head>
<body>
<main class="letterhead">
  <div class="brand-name">KORRO<span>INTERNATIONAL</span></div>
  <div class="header-divider"></div>
  <div class="header-info">
    <p class="header-tagline">Supply and Management of Infrastructure &amp; Logistic</p>
    <p class="header-address">P.O Box 482 Ridgeview QLD 4410&nbsp; P.O Box 317 Merrow NSW 2290</p>
    <p class="header-contact"><b>Ph:</b> 0400 123 456<span class="gap"></span><b>Email:</b> hello@korro.com.au</p>
  </div>

  <div class="watermark" aria-hidden="true">
    <div class="watermark-name">KORRO</div>
    <div class="watermark-sub">INTERNATIONAL</div>
  </div>

  <svg class="footer-wave" viewBox="0 0 848 160" aria-hidden="true">
    <defs>
      <linearGradient id="wave-warm" x1="0" x2="1" y1="0" y2="0">
        <stop offset="0" stop-color="#f7901e"/>
        <stop offset="0.45" stop-color="#a98a5c"/>
        <stop offset="1" stop-color="#1f6f8f"/>
      </linearGradient>
      <linearGradient id="wave-cool" x1="0" x2="1" y1="0" y2="0.3">
        <stop offset="0" stop-color="#0e5a85"/>
        <stop offset="0.6" stop-color="#1a86b8"/>
        <stop offset="1" stop-color="#2aaee0"/>
      </linearGradient>
    </defs>
    <path d="M0,38 C160,8 330,20 470,75 C580,118 640,132 720,128 L720,160 L0,160 Z" fill="url(#wave-warm)"/>
    <path d="M0,64 C180,38 380,90 540,122 C660,146 760,120 848,80 L848,160 L0,160 Z" fill="url(#wave-cool)"/>
    <path d="M0,64 C180,38 380,90 540,122 C660,146 760,120 848,80" fill="none" stroke="#ffffff" stroke-width="2"/>
  </svg>

  <div class="footer-text">
    <p class="divisions">KORRO Film Services&nbsp; | KORRO Pilot Escorts</p>
    <p class="divisions">KORRO Tour Management | KORRO Driver</p>
    <p class="owner">are divisions of <b>Korro International Pty Ltd</b></p>
    <p class="registration">ACN 000 111 222 ABN 00 000 111 222</p>
  </div>
</main>
</body>
</html>
```